Portrait of a Learner Infographic

A portrait of a learner is an aspirational idea of the skills a student should have at graduation. "Learner" recognizes that learning continues after graduation.
An info graphic is needed to convey the skills that have been identified. A full version is needed that can be posted on classroom walls (11x17) and a simplified version to share on the website and any other means identified.
The Birchfield School District is in Concord, New Hampshire, the capital city for NH. The district serves 4,100 diverse students in seven schools and a regional career and technical education center.
The district's hex colors are Green: #007137 and Blue: #085bab
Each school has its own unique colors.
The design should be positive, aspirational and still professional.
Teachers, students and parents
Public school district

```html
<!DOCTYPE html>
<html lang="en">
<head>
<meta charset="utf-8">
<title>Portrait of a Learner – Birchfield School District</title>
<link rel="stylesheet" href="https://fonts.googleapis.com/css2?family=Exo+2:wght@300;400;700;800&family=Fira+Sans:wght@400&family=Tinos:wght@400&display=swap">
<style>
  :root {
    --page-bg: #e4e5e7;
    --paper: #ffffff;
    --navy: #1c3c78;
    --stripe-blue: #2a5cae;
    --stripe-green: #0f723b;
    --title-green: #17803d;
    --intro-grey: #555a60;
    --blue-main: #0462a5;
    --blue-dark: #055896;
    --green-bright: #09a74a;
    --green-deep: #1a8b45;
    --fig-blue: #2f4f8f;
    --fig-green: #3c9c5e;
    --white: #ffffff;
  }
  * { box-sizing: border-box; margin: 0; padding: 0; }
  html, body { width: 1200px; height: 1200px; overflow: hidden; }
  body { background: var(--page-bg); position: relative; font-family: "Exo 2", sans-serif; }

  .poster {
    position: absolute; left: 280px; top: 111px;
    width: 612px; height: 944px;
    background: var(--paper); overflow: hidden;
    box-shadow: 0 4px 18px rgba(0,0,0,.12);
  }
  .swooshes { position: absolute; inset: 0; width: 612px; height: 944px; }

  .brand {
    position: absolute; left: 44px; top: 56px;
    font-family: "Tinos", serif; font-size: 19px; color: var(--title-green);
    letter-spacing: .5px; white-space: nowrap;
  }

  .headline {
    position: absolute; left: 40px; top: 138px;
    font-weight: 800; font-size: 30px; line-height: 34px; color: var(--title-green);
    letter-spacing: .2px; white-space: nowrap;
  }
  .intro {
    position: absolute; left: 41px; top: 184px; width: 410px;
    font-weight: 300; font-size: 13.6px; line-height: 16.5px; color: var(--intro-grey);
  }

  .panel { position: absolute; left: 40px; width: 540px; display: grid; }
  .panel--creative { top: 272px; height: 182px; grid-template-columns: 199px repeat(3, 1fr); grid-template-rows: 95px 87px; }
  .panel--collab { top: 483px; height: 171px; grid-template-columns: 113px 114px 113px 200px; grid-template-rows: 171px; }
  .panel--self { top: 687px; height: 182px; grid-template-columns: 199px repeat(3, 1fr); grid-template-rows: 94px 88px; }

  .pillar { grid-column: 1; grid-row: 1 / 3; position: relative; color: var(--white); overflow: hidden; }
  .pillar-title { font-weight: 800; font-size: 15.5px; letter-spacing: .3px; white-space: nowrap; }
  .panel--creative .pillar { background: var(--blue-main); }
  .panel--creative .pillar-title { position: absolute; left: 16px; top: 15px; }
  .panel--self .pillar { background: var(--blue-main); }
  .panel--self .pillar-title { position: absolute; left: 0; right: 0; top: 20px; text-align: center; }
  .panel--collab .pillar { grid-column: 4; grid-row: 1; background: var(--green-deep); }
  .panel--collab .pillar-title { position: absolute; left: 0; right: 0; top: 18px; text-align: center; }

  .figure { position: absolute; border-radius: 6px; }
  .figure--idea { left: 32px; top: 46px; width: 145px; height: 136px; background: linear-gradient(160deg, #c7cfe8 0%, #5b79b4 100%); opacity: .55; }
  .figure--team { left: 4px; top: 46px; width: 192px; height: 125px; background: linear-gradient(160deg, #c8d0e6 0%, var(--fig-green) 100%); opacity: .6; }
  .figure--puzzle { left: 16px; top: 58px; width: 183px; height: 124px; background: linear-gradient(160deg, #8aa3cf 0%, var(--fig-blue) 100%); opacity: .6; }

  .trait {
    color: var(--white); text-align: center;
    padding: 14px 5px 0; display: flex; flex-direction: column; align-items: center;
  }
  .trait-name { font-weight: 700; font-size: 9.6px; line-height: 12px; letter-spacing: .2px; min-height: 26px; display: flex; align-items: center; }
  .trait-text { font-family: "Fira Sans", sans-serif; font-size: 5.6px; line-height: 7.2px; margin-top: 5px; max-width: 80px; }

  .tone-a { background: var(--blue-dark); }
  .tone-b { background: var(--blue-main); }
  .tone-g1 { background: var(--green-bright); }
  .tone-g2 { background: var(--green-deep); }
  .tone-empty { background: transparent; }

  .panel--collab .trait { padding-top: 29px; }
  .panel--collab .trait-text { margin-top: 16px; max-width: 84px; }
  .panel--self .trait { padding-top: 8px; }
  .panel--self .trait-name { min-height: 22px; }
</style>
</head>
<body>
  <main class="poster">
    <svg class="swooshes" viewBox="0 0 612 944" aria-hidden="true">
      <path d="M318 0 C470 80 572 225 602 364 L612 364 L612 0 Z" fill="var(--stripe-blue)"/>
      <path d="M283 0 C440 30 560 150 612 282 L612 0 Z" fill="var(--stripe-green)"/>
      <path d="M330 0 C470 60 575 180 612 245 L612 0 Z" fill="var(--stripe-blue)"/>
      <path d="M380 0 C490 45 575 140 612 210 L612 0 Z" fill="var(--navy)"/>
      <path d="M15 410 C25 440 35 465 47 483" stroke="var(--stripe-blue)" stroke-width="4" fill="none"/>
      <path d="M0 528 C110 760 300 910 484 944 L0 944 Z" fill="var(--stripe-green)"/>
      <path d="M0 570 C120 790 260 900 379 944 L0 944 Z" fill="var(--stripe-blue)"/>
      <path d="M0 640 C120 820 220 905 304 944 L0 944 Z" fill="var(--navy)"/>
    </svg>

    <div class="brand">BIRCHFIELD SCHOOL DISTRICT</div>

    <h1 class="headline">PORTRAIT OF A LEARNER</h1>
    <p class="intro">Birchfield School District learners are informed, compassionate and capable citizens who effectively, courageously and responsibly direct their lives and positively impact communities</p>

    <section class="panel panel--creative">
      <div class="pillar">
        <h2 class="pillar-title">CREATIVE &amp; SKILLFUL</h2>
        <div class="figure figure--idea" role="img" aria-label="Illustration of a student with a light bulb idea"></div>
      </div>
      <div class="trait tone-a"><h3 class="trait-name">CRITICAL &amp;<br>ANALYTICAL THINKER</h3><p class="trait-text">Accesses, evaluates, applies and communicates diverse forms of information for a variety of audiences and purposes</p></div>
      <div class="trait tone-b"><h3 class="trait-name">INFORMED<br>RISK-TAKER</h3><p class="trait-text">Accesses, evaluates, applies and communicates diverse forms of information for a variety of audiences and purposes</p></div>
      <div class="trait tone-a"><h3 class="trait-name">CURIOUS</h3><p class="trait-text">Accesses, evaluates, applies and communicates diverse forms of information for a variety of audiences and purposes</p></div>
      <div class="trait tone-b"><h3 class="trait-name">INNOVATIVE</h3><p class="trait-text">Accesses, evaluates, applies and communicates diverse forms of information for a variety of audiences and purposes</p></div>
      <div class="trait tone-a"><h3 class="trait-name">ADAPTABLE</h3><p class="trait-text">Accesses, evaluates, applies and communicates diverse forms of information for a variety of audiences and purposes</p></div>
      <div class="trait tone-b"><h3 class="trait-name">SELF-MOTIVATED</h3><p class="trait-text">Accesses, evaluates, applies and communicates diverse forms of information for a variety of audiences and purposes</p></div>
    </section>

    <section class="panel panel--collab">
      <div class="trait tone-g1"><h3 class="trait-name">EMOTIONAL<br>INTELIGENCE</h3><p class="trait-text">Respectfully engages with others. Asks challenging and probing questions in a manner that preserves healthy relationships</p></div>
      <div class="trait tone-g2"><h3 class="trait-name">CIVIC MINDED</h3><p class="trait-text">Accesses, evaluates, applies and communicates diverse forms of information for a variety of audiences and purposes</p></div>
      <div class="trait tone-g1"><h3 class="trait-name">COMPASSIONATE<br>LEADER</h3><p class="trait-text">Accesses, evaluates, applies and communicates diverse forms of information for a variety of audiences and purposes</p></div>
      <div class="pillar">
        <h2 class="pillar-title">COLLABORATIVE</h2>
        <div class="figure figure--team" role="img" aria-label="Illustration of two students greeting each other"></div>
      </div>
    </section>

    <section class="panel panel--self">
      <div class="pillar">
        <h2 class="pillar-title">SELF-DIRECTED</h2>
        <div class="figure figure--puzzle" role="img" aria-label="Illustration of a student fitting puzzle pieces together"></div>
      </div>
      <div class="trait tone-a"><h3 class="trait-name">RESPONSIBLE</h3><p class="trait-text">Accesses, evaluates, applies and communicates diverse forms of information for a variety of audiences and purposes</p></div>
      <div class="trait tone-b"><h3 class="trait-name">SELF-STARTER</h3><p class="trait-text">Accesses, evaluates, applies and communicates diverse forms of information for a variety of audiences and purposes</p></div>
      <div class="trait tone-a"><h3 class="trait-name">GROWTH MNDSET</h3><p class="trait-text">Accesses, evaluates, applies and communicates diverse forms of information for a variety of audiences and purposes</p></div>
      <div class="trait tone-b"><h3 class="trait-name">PROBLEM SOLVING</h3><p class="trait-text">Accesses, evaluates, applies and communicates diverse forms of information for a variety of audiences and purposes</p></div>
      <div class="trait tone-a"><h3 class="trait-name">RESILIENT</h3><p class="trait-text">Accesses, evaluates, applies and communicates diverse forms of information for a variety of audiences and purposes</p></div>
      <div class="tone-empty"></div>
    </section>
  </main>
</body>
</html>
```